Tri-fold Brochure Design for Law Firm

I need a tri-fold brochure to give to prospective clients.
I have attached a Photoshop design file of a tri-fold brochure. The content (copy) is good, however, he brochure itself looks very amateurish.
I want a professional, sophisticated looking brochure.
The law firm specializes in commercial debt collection.
The law firm is located in New York City.
Our target market is business owners, doctors, lawyers, collection agencies and accountants.
Visit my website which is being designed at www.dorvenlaw.com. I like the font used for the name of my company and the rich blue color used.

Target Market(s)

Business Owners, Doctors, Law Firms and Accountants

Industry/Entity Type

Law Firm

Font styles to use
Serif

Requirements
Must have
• Professional quality graphic work. Attention to details.
• PHOTOGRAPHS ONLY, NO CLIP-ART.
• DARK COLORS - NAVY BLUE, HUNTER GREEN, BLACK, GRAY & WHITE
Nice to have
• I want it to look smart, modern and sophisticated.
• Visit my website which is being designed at www.dorvenlaw.com. I like the font used for the name of my company and the rich blue color used.
Should not have
• Bad artwork
• CLIP ART

```html
<!DOCTYPE html>
<html lang="en">
<head>
<meta charset="utf-8">
<title>Dorven Hale &amp; Company – Tri-fold Brochure</title>
<link rel="stylesheet" href="https://fonts.googleapis.com/css2?family=Cinzel:wght@400;500&family=Open+Sans:wght@400;600&family=Roboto:wght@400;700&display=swap">
<style>
:root{
  --navy:#26234f;
  --navy-deep:#1d1a40;
  --accent:#1a9be0;
  --ink:#1e1e2a;
  --lavender:#c9c3df;
  --white:#ffffff;
  --muted:#b9b6d4;
  --line:#8f8cb4;
}
*{box-sizing:border-box;margin:0;padding:0}
html,body{width:1200px;height:800px;overflow:hidden;background:#9a9a9a}
.brochure{display:flex;width:1200px;height:800px}
.panel{position:relative;width:400px;height:800px;overflow:hidden}

/* Inside panel */
.panel--about{background:var(--white);color:var(--ink);font-family:"Roboto",Arial,sans-serif}
.panel--about .edge{position:absolute;left:0;top:0;width:14px;height:100%;background:var(--navy)}
.panel--about .accent-shape{position:absolute;inset:0}
.statue{position:absolute;left:14px;bottom:60px;width:260px;height:340px;
  background:radial-gradient(ellipse at 45% 45%,#dcd6e7 0%,#eeebf4 55%,rgba(255,255,255,0) 75%);opacity:.9}
.about-content{position:relative;padding:40px 30px 0 40px}
.section-title{font-size:22px;font-weight:700;text-transform:uppercase;letter-spacing:.3px;color:var(--navy-deep);
  display:inline-block;border-bottom:2px solid var(--accent);padding-bottom:2px;margin-bottom:10px}
.section-title span{color:var(--accent)}
.intro{font-size:12.4px;line-height:1.45}
.serve-label{color:var(--accent);font-size:13px;margin:16px 0 4px}
.serve-list{list-style:none;font-size:13.5px;line-height:1.36}
.serve-list li::before{content:"•";margin-right:10px}
.why{margin-top:22px}
.why p{font-size:12.4px;line-height:1.38}
.bottom-rule{position:absolute;left:14px;right:0;bottom:50px;height:3px;background:var(--accent)}
.bottom-navy{position:absolute;right:0;bottom:0;width:200px;height:50px;background:var(--navy);clip-path:polygon(40% 0,100% 0,100% 100%,0 100%)}

/* Contact panel */
.panel--contact{background:var(--navy)}
.panel--contact .contact-bg{position:absolute;inset:0}
.contact-content{position:absolute;left:0;top:150px;width:330px;text-align:center;color:var(--white);font-family:"Open Sans",Arial,sans-serif}
.contact-heading{font-size:15px;font-weight:600;text-transform:uppercase;text-decoration:underline;text-underline-offset:3px;letter-spacing:.3px}
.contact-sub{font-size:10.5px}
.contact-block{margin-bottom:22px;font-size:13px;line-height:1.35}
.contact-web{font-size:16px;font-weight:600;margin:6px 0 24px}
.contact-phones{font-size:17px;font-weight:600;line-height:1.3;text-transform:uppercase}
.globe{position:absolute;left:183px;top:660px}
.footer-web{position:absolute;left:0;right:0;bottom:46px;text-align:center;color:var(--muted);font-family:"Open Sans",Arial,sans-serif;font-size:16px;letter-spacing:2px}

/* Cover panel */
.panel--cover{background:var(--navy)}
.cover-photo{position:absolute;left:0;top:0;width:400px;height:480px;
  background:linear-gradient(180deg,#5b6f8a 0%,#c99a86 26%,#8c8f9c 42%,#5d6677 65%,#3b4354 100%)}
.panel--cover .cover-shape{position:absolute;inset:0}
.cover-title{position:absolute;left:0;right:0;top:500px;text-align:center;color:var(--white);font-family:"Cinzel",Georgia,serif}
.firm-name{font-size:31px;font-weight:400;line-height:1.15;letter-spacing:1px}
.firm-name small{font-size:13px;vertical-align:top}
.firm-tag{font-size:14px;letter-spacing:1px;margin-top:8px;padding-bottom:10px;border-bottom:1px solid var(--line);display:inline-block}
.cover-phone{font-family:"Open Sans",Arial,sans-serif;font-size:30px;color:#d7d5ea;margin-top:14px;letter-spacing:1px}
.cover-web{font-family:"Open Sans",Arial,sans-serif;font-size:14px;color:var(--muted);letter-spacing:1px;margin-top:4px}
</style>
</head>
<body>
<main class="brochure">

  <section class="panel panel--about">
    <div class="edge"></div>
    <svg class="accent-shape" width="400" height="800" viewBox="0 0 400 800" aria-hidden="true">
      <polygon points="14,370 60,335 60,405" fill="var(--lavender)"/>
      <polygon points="14,735 34,748 14,750" fill="var(--lavender)"/>
    </svg>
    <div class="statue" role="img" aria-label="Faded photograph of a classical justice statue"></div>
    <div class="about-content">
      <h2 class="section-title">A Trusted <span>Partner</span></h2>
      <p class="intro">We under the business of debt collection. Our primary focus is to help our clients secure the payments they are owed. We work closely with both private clients and leading service professionals, such as attorneys and accountants, to provide added value to their clients through customized debt collection services.<br>We value our relationships as trusted advisors.</p>
      <p class="serve-label">We proudly serve:</p>
      <ul class="serve-list">
        <li>Law firms</li>
        <li>Accounting Firms</li>
        <li>Manufacturers</li>
        <li>Wholesalers and Distributors</li>
        <li>Collection Agencies</li>
        <li>Financial Service Companies</li>
        <li>Factors</li>
        <li>Doctors and Healthcare Professionals</li>
        <li>Carting Companies</li>
        <li>Oil Companies</li>
        <li>Freight Forwarders &amp; Custom Brokers</li>
        <li>Publishing and Advertising Companies</li>
        <li>Construction and Real Estate Firms</li>
      </ul>
      <div class="why">
        <h2 class="section-title">Why <span>Use Us</span></h2>
        <p>Anyone can sue a Debtor.</p>
        <p>It's not difficult to get nasty or to treat people who owe you money in a rude and unprofessional way.</p>
        <p>However, very few people have the skill, temperament and experience needed to effectively negotiate with Debtors, stakeholders, lawyers, as well as, court personnel, sheriffs and bankers to efficiently collect the most money possible in the least amount of time.</p>
        <p>We truly understand the nature of commercial debt. Collecting money is a specialized skill.</p>
      </div>
    </div>
    <div class="bottom-rule"></div>
    <div class="bottom-navy"></div>
  </section>

  <section class="panel panel--contact">
    <svg class="contact-bg" width="400" height="800" viewBox="0 0 400 800" aria-hidden="true">
      <defs>
        <linearGradient id="contactBlue" x1="0" y1="0" x2="1" y2="1">
          <stop offset="0" stop-color="#1a5fb4"/>
          <stop offset="0.5" stop-color="#1f8fd6"/>
          <stop offset="1" stop-color="#2ab4ec"/>
        </linearGradient>
      </defs>
      <path d="M0,120 C110,40 230,0 320,0 C380,220 385,480 300,660 C200,650 90,680 0,720 Z" fill="url(#contactBlue)"/>
      <path d="M330,0 L400,0 L400,60 Z" fill="var(--lavender)" opacity=".6"/>
    </svg>
    <div class="contact-content">
      <div class="contact-block">
        <div class="contact-heading">Dorven Hale &amp; Company, PLLC</div>
        <div class="contact-sub">Debt Collection Attorneys in New York State</div>
      </div>
      <div class="contact-web">www.DorvenLaw.com</div>
      <div class="contact-block">
        <div class="contact-heading">Marcus J. Dorven, Esquire</div>
        <div>President</div>
        <div>mdorven@dorvenlaw.com</div>
        <div>(212) 555-0193 Cell</div>
      </div>
      <div class="contact-block">
        <div class="contact-heading">Westchester County Office</div>
        <div>450 HARBOR VIEW AVENUE, SUITE 210</div>
        <div>WHITE PLAINS, NEW YORK 10601</div>
        <div>(Off Exit 7 on Route 119)</div>
      </div>
      <div class="contact-block">
        <div class="contact-heading">Mailing Address</div>
        <div>315 LEXINGTON ROW, SUITE 1820</div>
        <div>NEW YORK, NEW YORK 10016-2204</div>
      </div>
      <div class="contact-phones">
        <div>Toll Free: (877) 555-0142</div>
        <div>Local: (212) 555-0168</div>
        <div>Fax: (917) 555-0118</div>
      </div>
    </div>
    <svg class="globe" width="34" height="34" viewBox="0 0 34 34" aria-hidden="true">
      <circle cx="17" cy="17" r="16" fill="none" stroke="var(--line)" stroke-width="1.5"/>
      <circle cx="17" cy="17" r="10" fill="none" stroke="var(--line)" stroke-width="1.5"/>
      <ellipse cx="17" cy="17" rx="4" ry="10" fill="none" stroke="var(--line)" stroke-width="1.2"/>
      <line x1="7" y1="17" x2="27" y2="17" stroke="var(--line)" stroke-width="1.2"/>
    </svg>
    <div class="footer-web">www.dorvenlaw.com</div>
  </section>

  <section class="panel panel--cover">
    <div class="cover-photo" role="img" aria-label="Photograph of the New York City skyline at dusk with a tall art deco skyscraper"></div>
    <svg class="cover-shape" width="400" height="800" viewBox="0 0 400 800" aria-hidden="true">
      <path d="M0,480 C120,430 260,360 400,300 L400,800 L0,800 Z" fill="var(--navy)"/>
      <path d="M0,478 C120,428 260,358 400,298" fill="none" stroke="#5a5788" stroke-width="2"/>
    </svg>
    <div class="cover-title">
      <div class="firm-name">Dorven Hale<br>&amp; Company <small>PLLC</small></div>
      <div class="firm-tag">Debt Collection Attorneys</div>
      <div class="cover-phone">(877) 555-0142</div>
      <div class="cover-web">www.dorvenlaw.com</div>
    </div>
  </section>

</main>
</body>
</html>
```